OpenCart website

We have an existing site that was based on open cart in 2011 but customised heavily. We want a brand new open cart site designed from scratch so we can work on transitioning the existing opencart database over after the project is done

Current site: www.tallowfinchgoods.com

```html
<!DOCTYPE html>
<html lang="en">
<head>
<meta charset="utf-8">
<title>Tallowfinch Goods – Home</title>
<link href="https://fonts.googleapis.com/css2?family=Montserrat:wght@400;500;600;700;800&family=Open+Sans:wght@400;600;700&display=swap" rel="stylesheet">
<style>
:root{
  --red:#e31b23;
  --dark:#2b2b2b;
  --darker:#222;
  --ink:#1d1d1d;
  --muted:#555;
  --line:#d8d8d8;
  --panel:#efefef;
  --white:#fff;
  --star:#f3a712;
}
*{margin:0;padding:0;box-sizing:border-box}
html,body{width:1200px;height:3226px;overflow:hidden;background:var(--white)}
body{position:relative;font-family:"Open Sans",Arial,sans-serif;color:var(--ink)}
.abs{position:absolute}

/* header */
.topbar{left:0;top:0;width:1200px;height:97px;background:var(--white)}
.menu-zone{left:0;top:0;width:254px;height:97px;background:var(--dark);color:#fff;display:flex;align-items:center;justify-content:center;gap:10px;font:700 14px "Montserrat",sans-serif;letter-spacing:.5px}
.bag-zone{left:946px;top:0;width:254px;height:97px;background:var(--dark);color:#fff;display:flex;align-items:center;justify-content:center;gap:10px;font:700 14px "Montserrat",sans-serif;letter-spacing:.5px}
.brand{left:500px;top:22px;width:200px;text-align:center;font:800 26px/26px "Montserrat",sans-serif;color:var(--red);text-transform:uppercase}
.brand span{display:block}
.search{left:768px;top:34px;width:160px;height:30px;display:flex;align-items:center;justify-content:space-between;font-size:14px;color:#555}

/* hero */
.hero{left:0;top:97px;width:1200px;height:516px;background:linear-gradient(90deg,#f0f0f0 0%,#e2e2e2 60%,#d6d6d6 100%)}
.hero-title{left:118px;top:200px;font:800 86px/74px "Montserrat",sans-serif;color:var(--red);letter-spacing:-1px}
.hero-sub{left:120px;top:346px;font:800 28px "Montserrat",sans-serif;color:var(--ink)}
.hero-btn{left:120px;top:400px;width:149px;height:43px;background:var(--dark);color:#fff;font:700 14px/43px "Montserrat",sans-serif;text-align:center}
.hero-visual{left:527px;top:161px;width:591px;height:387px;border-radius:8px;background:radial-gradient(circle at 70% 50%,#e9e9ea 0%,#cfd0d2 55%,#dedede 100%)}
.hero-arrow{top:333px;width:44px;height:44px;border-radius:50%;background:#fff;box-shadow:0 1px 4px rgba(0,0,0,.25)}

/* categories */
.cat{top:652px;width:329px;height:344px}
.cat-label{position:absolute;left:0;right:0;top:244px;text-align:center;font:700 17px "Montserrat",sans-serif;color:var(--red)}
.cat-label span{background:rgba(255,255,255,.85);padding:4px 6px}
.cat-count{position:absolute;right:24px;top:286px;background:#111;color:#fff;font:700 11px/30px "Montserrat",sans-serif;padding:0 10px}

/* products */
.section-title{left:0;top:1048px;width:1200px;text-align:center;font:600 38px "Montserrat",sans-serif}
.tabs{left:312px;top:1121px;display:flex;font:600 12px "Montserrat",sans-serif}
.tab{height:31px;line-height:31px;padding:0 16px;color:#333}
.tab.on{background:var(--red);color:#fff}
.prod{width:239px}
.prod-img{width:239px;height:269px;background:var(--panel)}
.prod-name{margin-top:16px;font:700 14px "Montserrat",sans-serif;color:var(--ink)}
.prod-meta{display:flex;justify-content:space-between;align-items:center;margin-top:3px}
.price{font:700 14px "Montserrat",sans-serif;color:var(--red)}
.stars{display:flex;gap:2px}

/* brands */
.brands{left:75px;top:1965px;display:flex;gap:15px}
.brand-box{width:163px;height:86px;border:1px solid var(--line);display:flex;align-items:center;justify-content:center;font:700 15px "Montserrat",sans-serif;color:var(--red)}

/* blog + testimonial */
.post-cell{width:256px;height:210px}
.post-text{background:var(--panel);padding:16px 16px}
.post-date{font:700 30px "Montserrat",sans-serif;color:#222}
.post-date small{font-size:13px;font-weight:600}
.post-title{font:700 13px "Montserrat",sans-serif;margin-top:6px}
.post-body{font-size:12.5px;line-height:19px;color:#444;margin-top:6px}
.post-more{font:700 11px "Montserrat",sans-serif;color:var(--red);margin-top:8px}
.testi{left:826px;top:2129px;width:299px;height:393px;background:#fff;text-align:center}
.testi-text{position:absolute;left:18px;right:18px;top:226px;font-size:13.5px;line-height:24px;color:#444}
.testi-name{position:absolute;left:0;right:0;top:314px;font:700 14px "Montserrat",sans-serif;color:var(--red)}

/* features */
.feature{top:2608px;width:260px;text-align:center}
.feature-title{margin-top:22px;font:700 14px "Montserrat",sans-serif}
.feature-sub{margin-top:6px;font-size:13px;color:#444}

/* footer */
.footer{left:0;top:2782px;width:1200px;height:372px;background:var(--dark)}
.foot-col{top:2832px;color:#fff}
.foot-col h4{font:700 16px "Montserrat",sans-serif;margin-bottom:22px}
.foot-col li{list-style:none;font-size:13.5px;height:48px;display:flex;align-items:center;gap:12px;color:#e8e8e8;margin-top:-12px}
.news{left:793px;top:2782px;width:332px;height:372px;background:var(--red);color:#fff;text-align:center}
.news h4{margin-top:50px;font:700 16px "Montserrat",sans-serif}
.news-input{margin:22px auto 0;width:286px;height:41px;border:2px solid #fff;font-size:13.5px;line-height:37px}
.news-btn{margin:10px auto 0;width:114px;height:41px;background:var(--dark);font:700 14px/41px "Montserrat",sans-serif}
.news h5{margin-top:58px;font:700 16px "Montserrat",sans-serif}
.cards{display:flex;justify-content:center;gap:8px;margin-top:20px}
.card{width:38px;height:22px;background:#fff;border-radius:3px;color:var(--red);font:700 8px/22px "Open Sans",sans-serif}
.copyright{left:75px;top:3184px;font-size:12px;color:#333}
</style>
</head>
<body>

<header>
  <div class="abs topbar"></div>
  <div class="abs menu-zone">
    <svg width="14" height="12" viewBox="0 0 14 12"><rect y="0" width="14" height="2" fill="#fff"/><rect y="5" width="14" height="2" fill="#fff"/><rect y="10" width="14" height="2" fill="#fff"/></svg>
    MENU
  </div>
  <div class="abs brand"><span>Tallowfinch</span><span>Goods</span></div>
  <div class="abs search">Search...
    <svg width="14" height="14" viewBox="0 0 14 14"><circle cx="6" cy="6" r="4.5" fill="none" stroke="#333" stroke-width="2"/><line x1="9.5" y1="9.5" x2="13" y2="13" stroke="#333" stroke-width="2"/></svg>
  </div>
  <div class="abs bag-zone">
    <svg width="16" height="14" viewBox="0 0 16 14"><path d="M0 1h3l2 8h9l2-6H5" fill="none" stroke="#fff" stroke-width="1.8"/><circle cx="6" cy="12" r="1.4" fill="#fff"/><circle cx="13" cy="12" r="1.4" fill="#fff"/></svg>
    YOUR BAG
    <svg width="9" height="6" viewBox="0 0 9 6"><path d="M1 1l3.5 3.5L8 1" fill="none" stroke="#fff" stroke-width="1.5"/></svg>
  </div>
</header>

<section class="hero-area">
  <div class="abs hero"></div>
  <div class="abs hero-title">KITCHEN<br>SET SS</div>
  <div class="abs hero-sub">23PCS</div>
  <div class="abs hero-btn">CLICK MORE</div>
  <div class="abs hero-visual" role="img" aria-label="Boxed 23-piece stainless steel kitchen set with red utensils, colander and mixing bowls with red lids"></div>
  <svg class="abs hero-arrow" style="left:47px" viewBox="0 0 44 44"><circle cx="22" cy="22" r="22" fill="#fff"/><path d="M25 14l-8 8 8 8" fill="none" stroke="#333" stroke-width="3"/></svg>
  <svg class="abs hero-arrow" style="left:1107px" viewBox="0 0 44 44"><circle cx="22" cy="22" r="22" fill="#fff"/><path d="M19 14l8 8-8 8" fill="none" stroke="#333" stroke-width="3"/></svg>
</section>

<section class="categories">
  <div class="abs cat" style="left:75px;background:linear-gradient(160deg,#cfe4ef,#3f88c5 60%,#e07b2a)" role="img" aria-label="Colourful cleaning bottles and gloves in a blue basket">
    <div class="cat-label"><span>CLEANING SUPPLIES</span></div><div class="cat-count">07+ ITEMS</div>
  </div>
  <div class="abs cat" style="left:436px;background:linear-gradient(180deg,#3a3a3a,#8a8d90 55%,#bfc2c5)" role="img" aria-label="Hanging stainless steel kitchen utensils">
    <div class="cat-label"><span>STAINLESS STEEL</span></div><div class="cat-count">07+ ITEMS</div>
  </div>
  <div class="abs cat" style="left:796px;background:linear-gradient(150deg,#6b4a2b,#b58a55 50%,#d9b23a)" role="img" aria-label="Hammer, pliers and hand tools on wooden table">
    <div class="cat-label"><span>HARDWARE</span></div><div class="cat-count">07+ ITEMS</div>
  </div>
</section>

<section class="products">
  <h2 class="abs section-title">Our Products</h2>
  <div class="abs tabs">
    <div class="tab on">FEATURED PRODUCTS</div>
    <div class="tab">NEW ARRIVALS</div>
    <div class="tab">SHOP BY BRANDS</div>
    <div class="tab">BLACK FRIDAY SALE</div>
  </div>

  <svg width="0" height="0" style="position:absolute"><defs><symbol id="star" viewBox="0 0 12 12"><path d="M6 0.5l1.7 3.6 3.8.5-2.8 2.6.7 3.8L6 9.2 2.6 11l.7-3.8L.5 4.6l3.8-.5z" fill="#f3a712"/></symbol></defs></svg>

  <div class="abs prod" style="left:75px;top:1200px"><div class="prod-img" role="img" aria-label="Spice jar with seasoning"></div><div class="prod-name">PRODUCT NAME</div><div class="prod-meta"><span class="price">$8.00</span><span class="stars"><svg width="13" height="13"><use href="#star"/></svg><svg width="13" height="13"><use href="#star"/></svg><svg width="13" height="13"><use href="#star"/></svg><svg width="13" height="13"><use href="#star"/></svg><svg width="13" height="13"><use href="#star"/></svg></span></div></div>
  <div class="abs prod" style="left:346px;top:1200px"><div class="prod-img" role="img" aria-label="Cast iron dutch oven pot with handle"></div><div class="prod-name">PRODUCT NAME</div><div class="prod-meta"><span class="price">$8.00</span><span class="stars"><svg width="13" height="13"><use href="#star"/></svg><svg width="13" height="13"><use href="#star"/></svg><svg width="13" height="13"><use href="#star"/></svg><svg width="13" height="13"><use href="#star"/></svg><svg width="13" height="13"><use href="#star"/></svg></span></div></div>
  <div class="abs prod" style="left:617px;top:1200px"><div class="prod-img" role="img" aria-label="Three jars of scented air freshener gel"></div><div class="prod-name">PRODUCT NAME</div><div class="prod-meta"><span class="price">$8.00</span><span class="stars"><svg width="13" height="13"><use href="#star"/></svg><svg width="13" height="13"><use href="#star"/></svg><svg width="13" height="13"><use href="#star"/></svg><svg width="13" height="13"><use href="#star"/></svg><svg width="13" height="13"><use href="#star"/></svg></span></div></div>
  <div class="abs prod" style="left:888px;top:1200px"><div class="prod-img" role="img" aria-label="Five-piece paint roller set in red packaging"></div><div class="prod-name">PRODUCT NAME</div><div class="prod-meta"><span class="price">$8.00</span><span class="stars"><svg width="13" height="13"><use href="#star"/></svg><svg width="13" height="13"><use href="#star"/></svg><svg width="13" height="13"><use href="#star"/></svg><svg width="13" height="13"><use href="#star"/></svg><svg width="13" height="13"><use href="#star"/></svg></span></div></div>

  <div class="abs prod" style="left:75px;top:1574px"><div class="prod-img" role="img" aria-label="Grey swing-lid waste bin"></div><div class="prod-name">PRODUCT NAME</div><div class="prod-meta"><span class="price">$8.00</span><span class="stars"><svg width="13" height="13"><use href="#star"/></svg><svg width="13" height="13"><use href="#star"/></svg><svg width="13" height="13"><use href="#star"/></svg><svg width="13" height="13"><use href="#star"/></svg><svg width="13" height="13"><use href="#star"/></svg></span></div></div>
  <div class="abs prod" style="left:346px;top:1574px"><div class="prod-img" role="img" aria-label="Four patterned ceramic bowls"></div><div class="prod-name">PRODUCT NAME</div><div class="prod-meta"><span class="price">$8.00</span><span class="stars"><svg width="13" height="13"><use href="#star"/></svg><svg width="13" height="13"><use href="#star"/></svg><svg width="13" height="13"><use href="#star"/></svg><svg width="13" height="13"><use href="#star"/></svg><svg width="13" height="13"><use href="#star"/></svg></span></div></div>
  <div class="abs prod" style="left:617px;top:1574px"><div class="prod-img" role="img" aria-label="Packaged pumice stone"></div><div class="prod-name">PRODUCT NAME</div><div class="prod-meta"><span class="price">$8.00</span><span class="stars"><svg width="13" height="13"><use href="#star"/></svg><svg width="13" height="13"><use href="#star"/></svg><svg width="13" height="13"><use href="#star"/></svg><svg width="13" height="13"><use href="#star"/></svg><svg width="13" height="13"><use href="#star"/></svg></span></div></div>
  <div class="abs prod" style="left:888px;top:1574px"><div class="prod-img" role="img" aria-label="Set of printed ceramic mugs"></div><div class="prod-name">PRODUCT NAME</div><div class="prod-meta"><span class="price">$8.00</span><span class="stars"><svg width="13" height="13"><use href="#star"/></svg><svg width="13" height="13"><use href="#star"/></svg><svg width="13" height="13"><use href="#star"/></svg><svg width="13" height="13"><use href="#star"/></svg><svg width="13" height="13"><use href="#star"/></svg></span></div></div>
</section>

<section class="abs brands">
  <div class="brand-box">Glassmere</div>
  <div class="brand-box">Sunburst</div>
  <div class="brand-box">Stowell</div>
  <div class="brand-box">Hearth &amp; Co</div>
  <div class="brand-box">Forgeline</div>
  <div class="brand-box">Brightvolt</div>
</section>

<section class="blog">
  <div class="abs post-cell" style="left:75px;top:2103px;background:linear-gradient(135deg,#0b0b14,#3a1440 60%,#14141c)" role="img" aria-label="Neon Black Friday sale sign"></div>
  <div class="abs post-cell post-text" style="left:331px;top:2103px">
    <div class="post-date">21 <small>NOV, 2018</small></div>
    <div class="post-title">LOREM IPSUM DOLOR..</div>
    <div class="post-body">Nunc at tortor urna. Ut id eros eget turpis ultricies faucibus lobortis vitae metus venenatis..</div>
    <div class="post-more">READ MORE</div>
  </div>
  <div class="abs post-cell post-text" style="left:75px;top:2313px">
    <div class="post-date">21 <small>NOV, 2018</small></div>
    <div class="post-title">LOREM IPSUM DOLOR..</div>
    <div class="post-body">Nunc at tortor urna. Ut id eros eget turpis ultricies faucibus lobortis vitae metus venenatis..</div>
    <div class="post-more">READ MORE</div>
  </div>
  <div class="abs post-cell" style="left:331px;top:2313px;background:linear-gradient(135deg,#e6e3dc,#9aa0a4 50%,#4d6a5c)" role="img" aria-label="Stainless steel travel tumblers on a table"></div>

  <div class="abs" style="left:613px;top:2103px;width:512px;height:419px;background:linear-gradient(180deg,#d7d4cf,#b9b2a6 60%,#8e8577)" role="img" aria-label="Metal utensil holder with kitchen tools"></div>
  <div class="abs testi">
    <div class="abs" style="left:87px;top:38px;width:130px;height:130px;border-radius:50%;background:linear-gradient(180deg,#6a5a50,#c9b3a3)" role="img" aria-label="Customer portrait"></div>
    <svg class="abs" style="left:226px;top:24px" width="58" height="48" viewBox="0 0 58 48"><path d="M4 4h20v20l-8 20H6l6-20H4z M32 4h20v20l-8 20H34l6-20h-8z" fill="#cfcfcf"/></svg>
    <p class="testi-text">Nam mollis, eros in maximus tincidunt, urna nibh dictum dolor, at dictum sapien turpis eu dolor..”</p>
    <div class="testi-name">NAME HEADING</div>
  </div>
</section>

<section class="features">
  <div class="abs feature" style="left:64px">
    <svg width="50" height="40" viewBox="0 0 50 40"><rect x="2" y="6" width="28" height="22" fill="#e31b23"/><path d="M30 12h10l8 9v7H30z" fill="#e31b23"/><circle cx="12" cy="31" r="5" fill="#e31b23" stroke="#fff" stroke-width="2"/><circle cx="38" cy="31" r="5" fill="#e31b23" stroke="#fff" stroke-width="2"/></svg>
    <div class="feature-title">FREE WORLD DELIVERY</div><div class="feature-sub">On Order Over $100</div>
  </div>
  <div class="abs feature" style="left:332px">
    <svg width="50" height="48" viewBox="0 0 50 48"><text x="25" y="42" text-anchor="middle" font-family="Montserrat,sans-serif" font-weight="700" font-size="46" fill="#e31b23">$</text></svg>
    <div class="feature-title" style="margin-top:14px">MONEYBACK GUARANTEE</div><div class="feature-sub">Best Deal With 30days</div>
  </div>
  <div class="abs feature" style="left:603px">
    <svg width="56" height="40" viewBox="0 0 56 40"><ellipse cx="22" cy="16" rx="18" ry="13" fill="#e31b23"/><path d="M10 26l-4 10 12-7z" fill="#e31b23"/><ellipse cx="38" cy="22" rx="14" ry="10" fill="#e31b23" stroke="#fff" stroke-width="2"/></svg>
    <div class="feature-title">BEST ONLINE SUPPORT</div><div class="feature-sub">Hours : 8am-11pm</div>
  </div>
  <div class="abs feature" style="left:874px">
    <svg width="50" height="42" viewBox="0 0 50 42"><path d="M14 2h22v12a11 11 0 0 1-22 0z" fill="#e31b23"/><path d="M14 6H6v4a8 8 0 0 0 8 8M36 6h8v4a8 8 0 0 1-8 8" fill="none" stroke="#e31b23" stroke-width="3"/><rect x="22" y="24" width="6" height="8" fill="#e31b23"/><rect x="15" y="32" width="20" height="6" fill="#e31b23"/></svg>
    <div class="feature-title">WIN $100 TO SHOP</div><div class="feature-sub">Get Membership</div>
  </div>
</section>

<footer>
  <div class="abs footer"></div>
  <div class="abs foot-col" style="left:75px">
    <h4>INFORMATION</h4>
    <ul><li>About Us</li><li>Locations &amp; Contacts</li><li>Terms Of Use</li><li>Site Map</li></ul>
  </div>
  <div class="abs foot-col" style="left:286px">
    <h4>QUICK LINKS</h4>
    <ul><li>My Account</li><li>Create Account</li><li>My Shopping List</li><li>Credit Application &amp; Prepaid Shipping</li></ul>
  </div>
  <div class="abs foot-col" style="left:606px">
    <h4>FOLLOW US</h4>
    <ul>
      <li><svg width="10" height="10"><circle cx="5" cy="5" r="4" fill="#fff"/></svg>Circlepage</li>
      <li><svg width="10" height="10"><circle cx="5" cy="5" r="4" fill="#fff"/></svg>Chirpline</li>
      <li><svg width="10" height="10"><rect x="1" y="1" width="8" height="8" fill="#fff"/></svg>Snapgrid</li>
    </ul>
  </div>
  <div class="abs news">
    <h4>NEWSLETTER SIGN UP</h4>
    <div class="news-input">Enter Email Address</div>
    <div class="news-btn">SIGN UP</div>
    <h5>PAYMENT METHOD</h5>
    <div class="cards"><div class="card">Paylo</div><div class="card">Norra</div><div class="card">Mint</div><div class="card">Amber</div><div class="card">Cirrum</div></div>
  </div>
  <p class="abs copyright">Copyright © 2018 Tallowfinch Goods Imports Inc. All Rights Reserved</p>
</footer>

</body>
</html>
```